Flyer-Design für  Kampfsportschule
Flyer-Design für Kampfsportschule
Zielgruppe
Wir bieten Taekwondo/Selbstverteidigung an. Meine Zielgruppe sind Erwachsene ab 17 Jahren.
Aufgabenstellung
Das Angebot '1 Monat kostenloses Training, oder einen Monat kostenloses Training' und 'Taekwondo/Selbstverteidigung in Weinstadt' soll eingebracht und direkt sichtbar sein. Eventuell auch Punkte wie Selbstbewusstsein, Beweglichkeit, Zielstrebigkeit, Kraft und Ausdauer, körperliche Fitness... Farben: Weiß, schwarz und Schrift in gelb. Nichts rotes.
Die Daten:
Tel: 0176-4918257 Email: m.r.budozentrum@postfach-beispiel.de und www.mrbudozentrum-beispiel.de

```html
<!DOCTYPE html>
<html lang="de">
<head>
<meta charset="utf-8">
<title>Flyer Selbstverteidigung Weinstadt</title>
<link href="https://fonts.googleapis.com/css2?family=Barlow+Condensed:wght@600;700&family=Source+Sans+3:wght@400;600;700&family=Open+Sans:wght@300;800&display=swap" rel="stylesheet">
<style>
  :root {
    --bg: #e6e7e6;
    --black: #050505;
    --ink: #0b0b0b;
    --yellow: #ecb732;
    --white: #f4f4f4;
    --photo-top: #5a5f66;
    --photo-mid: #2b2d31;
  }
  * { box-sizing: border-box; margin: 0; padding: 0; }
  html, body { width: 1200px; height: 1200px; overflow: hidden; background: var(--bg); }
  .flyer {
    position: absolute; left: 180px; top: 6px;
    width: 840px; height: 1188px;
    background: var(--black); overflow: hidden;
    font-family: "Source Sans 3", "Source Sans Pro", sans-serif;
    color: var(--white);
  }
  .hero-photo {
    position: absolute; left: 0; top: 0; width: 840px; height: 660px;
    background: radial-gradient(ellipse at 55% 35%, var(--photo-top) 0%, var(--photo-mid) 45%, var(--black) 100%);
  }
  .offer-badge {
    position: absolute; left: 510px; top: -110px;
    width: 300px; height: 300px; border-radius: 50%;
    background: var(--yellow); color: var(--white);
    display: flex; flex-direction: column; align-items: center; justify-content: flex-end;
    padding-bottom: 62px; font-family: "Open Sans", sans-serif; text-align: center;
  }
  .offer-badge .big { font-weight: 800; font-size: 40px; line-height: 1.1; }
  .offer-badge .small { font-weight: 300; font-size: 31px; line-height: 1.2; }
  .headline {
    position: absolute; left: 100px; top: 520px; width: 680px;
    font-family: "Barlow Condensed", sans-serif; font-weight: 700;
    text-align: right; line-height: 0.95;
  }
  .headline .main { display: block; color: var(--yellow); font-size: 88px; text-align: left; letter-spacing: 0.5px; }
  .headline .place { display: block; color: var(--white); font-size: 56px; font-weight: 600; }
  .intro {
    position: absolute; left: 104px; top: 680px; width: 400px;
    font-weight: 700; font-size: 21px; line-height: 1.6;
  }
  .accent { color: var(--yellow); }
  .body-copy {
    position: absolute; left: 104px; top: 762px; width: 660px;
    font-size: 16px; line-height: 1.75;
  }
  .body-copy p { margin-bottom: 22px; }
  .body-copy .accent { font-weight: 700; }
  .cta { font-weight: 700; font-size: 18px; line-height: 2.3; }
  .footer-name {
    position: absolute; left: 0; top: 1050px; width: 840px; height: 44px;
    background: var(--white); color: var(--ink);
    font-weight: 700; font-size: 20px; padding: 8px 0 0 96px;
  }
  .footer-contact {
    position: absolute; left: 0; top: 1094px; width: 840px; height: 94px;
    background: var(--yellow); color: var(--ink);
    font-weight: 600; font-size: 16px; line-height: 1.6;
    display: flex; gap: 32px; padding: 14px 0 0 96px;
  }
  .brand-seal {
    position: absolute; left: 610px; top: 930px;
    width: 210px; height: 210px; border-radius: 50%;
    background: var(--white); border: 10px solid var(--black);
    display: flex; align-items: center; justify-content: center; text-align: center;
    color: var(--ink); font-weight: 700; font-size: 22px; line-height: 1.2;
  }
</style>
</head>
<body>
  <main class="flyer">
    <div class="hero-photo" role="img" aria-label="Foto: Frau wehrt in einer Selbstverteidigungssituation einen Angreifer ab, dunkler Studiohintergrund"></div>

    <div class="offer-badge">
      <span class="big">1 Monat</span>
      <span class="small">kostenloses</span>
      <span class="small">Training</span>
    </div>

    <h1 class="headline">
      <span class="main">SELBSTVERTEIDIGUNG</span>
      <span class="place">in Weinstadt</span>
    </h1>

    <p class="intro"><span class="accent">SICHERHEIT</span> wird vor allem zur heutigen Zeit groß geschrieben!</p>

    <div class="body-copy">
      <p>Um Gefahren einzuschätzen, vermeiden, oder im Notfall auch abwehren zu können, bieten wir Ihnen effektive <span class="accent">Selbstverteidigungskurse</span> - individuell angepasst auf Ihre Gruppe.</p>
      <p>Egal ob eine Hobbygruppe, Firma, Sportvereine, Schulklassen, only Women, oder du alleine als Einzeltraining. Unsere Kurse bringen sich überall gut ein</p>
      <div class="cta">
        Sie möchten einen <span class="accent">Selbstverteidigungskurs</span> buchen?<br>
        Kontaktieren Sie uns um weitere Infos zu erhalten!
      </div>
    </div>

    <div class="footer-name">M.R.Budozentrum - Taekwondo Akademie Weinstadt</div>
    <div class="footer-contact">
      <div>Lindenweg 14 | 71384 Weinstadt<br>Tel: 0176-4918257</div>
      <div>m.r.budozentrum@postfach-beispiel.de<br>www.mrbudozentrum-beispiel.de</div>
    </div>

    <div class="brand-seal">MR<br>Budozentrum</div>
  </main>
</body>
</html>
```